Design a styled business card for an intimacy and attachment psychologist

I am a Psychologist providing online therapy to patients across the United States. My work is interpersonal and emotion-focused, with an emphasis on the client-therapist relationship. My primary areas of work are very personal, including sexuality and gender, abuse and trauma, and grief and loss. My target audience will be adults of all ages 18+.
My business card should convey a warm and inviting feeling of professionalism that is also casual and comfortable.
The front should be fairly simple and professional, consisting of:
- My name, Dr. Rosalind Pembrook
- My title, Licensed Psycholigist
- My logo
On either the front or the back, my contact information should be listed:
- ros@drrospembrook.example
- 555.014.7789
- drrospembrook.example
On the rear, I would like a description of the areas that I specialize in. This can be formatted in any way that appears stylistically interesting.
Individual and Couples
Relationships and Infidelity
Sexual Health & Aging
Gender Identity & Sexual Orientation
Abuse and Trauma
Sexual Compulsivity & Addiction
Sexual Dysfunction
Target Market(s)
My target audience will be adults of all ages 18+.
Industry/Entity Type
Psychology
Contact Information for Business Card
The front should be fairly simple and professional, consisting of: - My name, Dr. Rosalind Pembrook - My title, Licensed Psycholigist - My logo On either the front or the back, my contact information should be listed: - ros@drrospembrook.example - 555.014.7789 - drrospembrook.example On the rear, I would like a description of the areas that I specialize in. This can be formatted in any way that appears stylistically interesting. Individual and Couples Relationships and Infidelity Sexual Health & Aging Gender Identity & Sexual Orientation Abuse and Trauma Sexual Compulsivity & Addiction Sexual Dysfunction

```html
<!DOCTYPE html>
<html lang="en">
<head>
<meta charset="utf-8">
<title>Dr. Rosalind Pembrook – Business Card</title>
<link rel="stylesheet" href="https://fonts.googleapis.com/css2?family=Montserrat:wght@400;500;600;700&display=swap">
<style>
  :root {
    --stage: #333333;
    --card: #ffffff;
    --navy: #2a2350;
    --orange: #f5a21b;
    --teal: #5ec4ad;
    --ink: #1f1b3a;
  }
  * { box-sizing: border-box; margin: 0; padding: 0; }
  html, body {
    width: 1200px; height: 780px; overflow: hidden;
    background: var(--stage);
    font-family: "Montserrat", sans-serif;
  }
  .stage { position: relative; width: 1200px; height: 780px; }
  .card {
    position: absolute; top: 230px;
    width: 560px; height: 320px;
    background: var(--card);
    overflow: hidden;
    box-shadow: 0 10px 30px rgba(0,0,0,.45);
  }
  .card--brand { left: 30px; }
  .card--details { left: 610px; }

  /* brand side */
  .brand-lockup {
    position: absolute; left: 70px; top: 90px;
    display: flex; align-items: center; gap: 28px;
  }
  .brand-dot {
    width: 130px; height: 130px; border-radius: 50%;
    background: var(--teal);
    flex: none;
  }
  .brand-name {
    color: var(--navy); font-weight: 600;
    font-size: 32px; line-height: 1.15; letter-spacing: 1px;
    text-transform: uppercase;
  }

  /* details side */
  .contact-band { position: absolute; left: 0; top: 0; width: 560px; height: 320px; }

  .mini-lockup {
    position: absolute; left: 30px; top: 28px;
    display: flex; align-items: center; gap: 14px;
  }
  .mini-lockup .brand-dot { width: 70px; height: 70px; }
  .mini-lockup .brand-name { font-size: 18px; line-height: 1.1; }

  .specialties {
    position: absolute; right: 22px; top: 18px;
    text-align: right; list-style: none;
  }
  .specialties li {
    color: var(--ink); font-size: 10.5px; font-weight: 500; line-height: 1.35;
    display: flex; justify-content: flex-end; align-items: center; gap: 6px;
  }
  .specialties li::after {
    content: ""; width: 7px; height: 7px; border-radius: 50%;
    background: var(--teal); flex: none;
  }
  .specialties .specialties__heading {
    display: block;
    color: var(--orange); font-weight: 700; font-size: 13px;
    letter-spacing: .5px; margin-bottom: 3px; padding-right: 13px;
  }
  .specialties .specialties__heading::after { content: none; }

  .identity {
    position: absolute; left: 30px; top: 166px;
    padding-left: 12px;
    border-left: 7px solid var(--orange);
  }
  .identity__name { color: var(--orange); font-weight: 700; font-size: 22px; line-height: 1.15; }
  .identity__title { color: var(--ink); font-weight: 500; font-size: 15px; letter-spacing: .5px; margin-top: 2px; }

  .contact {
    position: absolute; left: 30px; top: 258px; list-style: none;
  }
  .contact li {
    display: flex; align-items: center; gap: 10px;
    color: #ffffff; font-size: 13px; font-weight: 500; line-height: 1.35;
    letter-spacing: .3px;
  }
  .contact svg { width: 13px; height: 13px; flex: none; }
</style>
</head>
<body>
<main class="stage">

  <section class="card card--brand" aria-label="Card front">
    <div class="brand-lockup">
      <span class="brand-dot"></span>
      <p class="brand-name">Dr.<br>Rosalind<br>Pembrook</p>
    </div>
  </section>

  <section class="card card--details" aria-label="Card back">
    <svg class="contact-band" viewBox="0 0 560 320" preserveAspectRatio="none" aria-hidden="true">
      <polygon points="0,250 560,185 560,320 0,320" fill="var(--navy)"/>
    </svg>

    <div class="mini-lockup">
      <span class="brand-dot"></span>
      <p class="brand-name">Dr.<br>Rosalind<br>Pembrook</p>
    </div>

    <ul class="specialties">
      <li class="specialties__heading">SPECIALIZE</li>
      <li>Abuse and Trauma</li>
      <li>Sexual Dysfunction</li>
      <li>Sexual Health &amp; Aging</li>
      <li>Stylistically interesting</li>
      <li>Individual and Couples</li>
      <li>Relationships and Infidelity</li>
      <li>Sexual Compulsivity &amp; Addiction</li>
      <li>Gender Identity &amp; Sexual Orientation</li>
    </ul>

    <div class="identity">
      <p class="identity__name">Dr. Rosalind Pembrook</p>
      <p class="identity__title">Licensed Psycholigist</p>
    </div>

    <ul class="contact">
      <li>
        <svg viewBox="0 0 24 24" aria-hidden="true"><path fill="var(--orange)" d="M6.6 10.8a15.1 15.1 0 0 0 6.6 6.6l2.2-2.2a1 1 0 0 1 1-.25 11.4 11.4 0 0 0 3.6.57 1 1 0 0 1 1 1V20a1 1 0 0 1-1 1A17 17 0 0 1 3 4a1 1 0 0 1 1-1h3.5a1 1 0 0 1 1 1c0 1.250.2 2.450.57 3.57a1 1 0 0 1-.25 1z"/></svg>
        555.014.7789
      </li>
      <li>
        <svg viewBox="0 0 24 24" aria-hidden="true"><rect x="2" y="5" width="20" height="14" rx="2" fill="var(--orange)"/><path d="M3 6l9 7 9-7" fill="none" stroke="var(--navy)" stroke-width="2"/></svg>
        ros@drrospembrook.example
      </li>
      <li>
        <svg viewBox="0 0 24 24" aria-hidden="true"><circle cx="12" cy="12" r="10" fill="var(--orange)"/><path d="M2 12h20M12 2c3 3 3 17 0 20M12 2c-3 3-3 17 0 20" fill="none" stroke="var(--navy)" stroke-width="1.5"/></svg>
        www.drrospembrook.example
      </li>
    </ul>
  </section>

</main>
</body>
</html>
```